Non-Fiction Book On Creativity - Cover Design / Physical and E-Book

I am looking for designs for my first book! It's called: Patience Builds Harbors. The subtitle is: 12 Chapters About Gathering Courage, Mending Fences, And Walking A Quiet Road.
It's a series of short lessons and principals on creativity and it will be a Vellora book and a physical book.
I'm really open to any type of designs but have attached some screenshots of other book covers that have a design and style that I like.
Please let me know if you have any questions or need any more information.
Creativity / Self-Help / Personal Development

```html
<!DOCTYPE html>
<html lang="en">
<head>
<meta charset="utf-8">
<title>Patience Builds Harbors — Book Cover</title>
<link rel="stylesheet" href="https://fonts.googleapis.com/css2?family=Barlow+Condensed:wght@600&family=Barlow:wght@600&family=Tinos&display=swap">
<style>
  :root {
    --backdrop: #b5b6b1;
    --paper: #ffffff;
    --band-edge: #7d1517;
    --band-mid: #c8103a;
    --title-yellow: #ffec00;
    --monogram-ink: #222220;
    --subtitle-brown: #5a4716;
    --author-ink: #1f1f1f;
    --art-gold: #e8c25c;
    --art-sand: #efe3bf;
    --art-stone: #d6d3ca;
    --art-ink: #8d8a82;
  }
  * { margin: 0; padding: 0; box-sizing: border-box; }
  html, body {
    width: 1200px; height: 1000px; overflow: hidden;
    background: var(--backdrop);
  }
  .canvas { position: relative; width: 1200px; height: 1000px; }
  .cover {
    position: absolute; left: 266px; top: 0;
    width: 668px; height: 1000px;
    background: var(--paper);
    overflow: hidden;
  }
  .cover-art {
    position: absolute; left: 128px; top: 8px;
    width: 540px; height: 432px;
    border-radius: 220px 0 0 0;
    background:
      radial-gradient(circle at 36% 62%, var(--art-gold) 0%, var(--art-sand) 22%, rgba(239,227,191,0) 48%),
      linear-gradient(160deg, var(--art-stone) 0%, #e4e1d9 45%, var(--art-ink) 140%);
  }
  .title-band {
    position: absolute; left: 0; top: 440px;
    width: 668px; height: 343px;
    background: linear-gradient(90deg, var(--band-edge) 0%, var(--band-mid) 50%, var(--band-edge) 100%);
    overflow: hidden;
  }
  .monogram {
    position: absolute; top: -82px;
    font-family: "Barlow Condensed", "Arial Narrow", sans-serif;
    font-weight: 600;
    font-size: 470px; line-height: 1;
    color: var(--monogram-ink);
  }
  .monogram-left { left: 46px; }
  .monogram-right { right: 30px; }
  .book-title {
    position: absolute; left: 0; top: 14px; width: 100%;
    text-align: center;
    font-family: "Barlow Condensed", "Arial Narrow", sans-serif;
    font-weight: 600;
    font-size: 106px; line-height: 101px;
    color: var(--title-yellow);
    text-transform: uppercase;
  }
  .subtitle {
    position: absolute; left: 0; top: 796px; width: 100%;
    text-align: center;
    font-family: "Tinos", "Times New Roman", serif;
    font-size: 26px; line-height: 33px;
    color: var(--subtitle-brown);
  }
  .author {
    position: absolute; left: 0; top: 941px; width: 100%;
    text-align: center;
    font-family: "Barlow", Arial, sans-serif;
    font-weight: 600;
    font-size: 22px; letter-spacing: 2px;
    color: var(--author-ink);
  }
</style>
</head>
<body>
<div class="canvas">
  <div class="cover">
    <div class="cover-art" role="img" aria-label="Line illustration of a hand placing a gold star into an open head"></div>
    <div class="title-band">
      <span class="monogram monogram-left" aria-hidden="true">P</span>
      <span class="monogram monogram-right" aria-hidden="true">H</span>
      <h1 class="book-title">Patience<br>Builds<br>Harbors</h1>
    </div>
    <p class="subtitle">12 Chapters About Gathering Courage,<br>Mending Fences,<br>And Walking A Quiet Road.</p>
    <p class="author">AUTHOR’S NAME</p>
  </div>
</div>
</body>
</html>
```